Wendmar Digital - Layout Design

We need a web design for a new company based in Australia, called "Wendmar Digital". We develop innovative custom web applications for Out Of Home, and Media companies.
Our initial website is a one page type of site. I've created a simple wireframe to show you what we need: https://sketchplot.example/qT4mZ9
Here is a layout reference: http://fernloft.example/
( note - the designs needs to follow our branding guidelines (attached).
The top feature could be just solid color or an abstract subtle pattern or illustration that conveys the specialization of our business in the area of out of home, map, data.
In the attachment you will also find some images added for the work section.
Media and Advertising
Digital
1 page

```html
<!DOCTYPE html>
<html lang="en">
<head>
<meta charset="utf-8">
<title>Wendmar Digital</title>
<link rel="stylesheet" href="https://fonts.googleapis.com/css2?family=Open+Sans:wght@300;400;600;700&display=swap">
<style>
:root{
  --red:#ef4b3a;
  --ink:#333a40;
  --text:#6f7479;
  --muted:#9a9ea2;
  --rule:#e3e3e3;
  --navy:#1d2533;
  --footer:#3b3b3d;
  --footer-deep:#2c2c2e;
  --white:#ffffff;
}
*{box-sizing:border-box;margin:0;padding:0}
html,body{width:1200px;height:3264px;overflow:hidden;background:var(--white)}
body{position:relative;font-family:"Open Sans",Arial,sans-serif;color:var(--text)}
.abs{position:absolute}

.topbar{left:0;top:0;width:1200px;height:24px;background:var(--red);color:var(--white);font-size:10px;display:flex;align-items:center;justify-content:space-between;padding:0 140px}
.topbar .call{display:flex;align-items:center;gap:6px;font-size:11px;font-weight:600}

.navbar{left:0;top:24px;width:1200px;height:96px;display:flex;align-items:center;justify-content:space-between;padding:0 135px}
.brand{font-size:30px;font-weight:600;color:var(--ink);letter-spacing:-0.5px}
.menu{display:flex;height:96px;align-items:stretch}
.menu a{display:flex;align-items:center;padding:0 13px;font-size:13px;font-weight:600;color:var(--ink);text-decoration:none}
.menu a.active{background:var(--red);color:var(--white)}

.hero{left:0;top:120px;width:1200px;height:465px;background:linear-gradient(90deg,#8d8f92 0%,#c9cbcd 30%,#eef0f1 55%,#f6f7f8 100%)}
.hero-copy{left:760px;top:100px;width:380px;font-size:33px;font-weight:300;line-height:1.3;color:var(--ink)}
.btn{left:917px;top:337px;width:140px;height:44px;background:var(--red);color:var(--white);font-size:15px;display:flex;align-items:center;justify-content:center}
.arrow{top:210px;width:20px;height:36px;background:#3c3c3c;display:flex;align-items:center;justify-content:center}

.section-title{left:0;width:1200px;text-align:center;font-size:40px;font-weight:300;color:var(--ink)}
.lede{left:135px;width:930px;text-align:center;font-size:11px;line-height:1.75;color:var(--muted)}
.rule{left:135px;width:930px;height:1px;background:var(--rule)}

.team-list{left:140px;top:978px;list-style:none}
.team-list li{display:flex;align-items:center;gap:10px;font-size:13px;color:var(--ink);height:34px}
.team-list li::before{content:"";width:14px;height:14px;background:#c9c9c9}
.team-list li.current{color:var(--red)}
.team-list li.current::before{background:var(--red)}
.profile{left:365px;top:985px;width:700px;height:205px;border:1px solid var(--rule);display:flex;gap:22px;padding:16px}
.portrait{width:160px;height:170px;flex:none;background:linear-gradient(160deg,#d9dcdf,#8b9097)}
.profile h3{font-size:14px;font-weight:600;color:var(--red);margin-bottom:8px}
.profile h3 span{font-size:10px;font-weight:400;color:var(--muted)}
.profile p{font-size:11px;line-height:1.7;color:var(--muted)}

.work{left:135px;top:1555px;width:930px;display:grid;grid-template-columns:465px 465px;grid-auto-rows:455px}
.card{display:flex;flex-direction:column}
.shot{height:325px}
.caption{flex:1;background:var(--navy);padding:16px 18px}
.caption h4{font-size:22px;font-weight:600;color:var(--white);margin-bottom:6px}
.caption.featured h4{color:#f47a3b}
.caption p{font-size:11px;line-height:1.6;color:#aab0ba}

.footer{left:0;top:2920px;width:1200px;height:344px;background:var(--footer);border-top:4px solid var(--red)}
.contact{left:135px;top:30px;width:300px;color:#d6d6d6}
.contact h5{font-size:17px;font-weight:600;color:var(--white);margin-bottom:6px}
.contact .intro{font-size:11px;line-height:1.5;color:#b9b9b9;margin-bottom:12px}
.contact .row{display:flex;gap:10px;font-size:11px;line-height:1.5;margin-bottom:10px}
.contact svg{flex:none;margin-top:2px}
.quote-form{left:535px;top:36px;width:430px;display:grid;grid-template-columns:205px 205px;gap:10px 20px}
.field{height:28px;background:#f2f2f2;font-size:10px;color:#8a8a8a;padding:0 10px;display:flex;align-items:center}
.field.tall{height:54px;align-items:flex-start;padding-top:8px}
.submit{width:70px;height:24px;background:var(--red);color:var(--white);font-size:10px;font-weight:600;display:flex;align-items:center;justify-content:center;align-self:end}
.copyright{left:0;bottom:0;width:1200px;height:40px;background:var(--footer-deep);color:#8e8e8e;font-size:10px;display:flex;align-items:center;justify-content:center}
</style>
</head>
<body>

<div class="abs topbar">
  <span>Connect with Us</span>
  <span class="call">
    <svg width="11" height="11" viewBox="0 0 24 24"><path fill="#fff" d="M6.6 10.8a15 15 0 0 0 6.6 6.6l2.2-2.2a1 1 0 0 1 1-.25 11.4 11.4 0 0 0 3.6.57 1 1 0 0 1 1 1V20a1 1 0 0 1-1 1A17 17 0 0 1 3 4a1 1 0 0 1 1-1h3.5a1 1 0 0 1 1 1c0 1.25.2 2.45.57 3.57a1 1 0 0 1-.25 1z"/></svg>
    Call: 123 456 789
  </span>
</div>

<header class="abs navbar">
  <div class="brand">Wendmar Digital</div>
  <nav class="menu">
    <a class="active">Home</a><a>About Us</a><a>Team</a><a>Services</a><a>Experience</a><a>Contact Us</a>
  </nav>
</header>

<section class="abs hero" role="img" aria-label="Smiling businessman working at a laptop in a bright office">
  <div class="abs arrow" style="left:0"><svg width="8" height="12" viewBox="0 0 8 12"><path d="M6 1 1 6l5 5" stroke="#fff" stroke-width="2" fill="none"/></svg></div>
  <div class="abs arrow" style="right:0"><svg width="8" height="12" viewBox="0 0 8 12"><path d="m2 1 5 5-5 5" stroke="#fff" stroke-width="2" fill="none"/></svg></div>
  <p class="abs hero-copy">We develop innovative custom web applications for Out Of Home, and Media companies.</p>
  <div class="abs btn">Get Started</div>
</section>

<h2 class="abs section-title" style="top:610px">About Us</h2>
<p class="abs lede" style="top:672px">Wendmar Digital builds custom web applications for outdoor advertising and media businesses. We pair clear data with careful design so that campaign teams can plan, book and report on their inventory in one place. Our small team works closely with each client, from the first sketch to launch and beyond, keeping tools fast, simple and easy to maintain. We favour open standards, honest timelines and software that grows with the people who use it every day, across screens, sites and regions throughout Australia and the wider region.</p>
<div class="abs rule" style="top:790px"></div>

<h2 class="abs section-title" style="top:830px">Our Team</h2>
<ul class="abs team-list">
  <li>Emily Harlow</li>
  <li>Brian Tolle</li>
  <li class="current">Martin Averly</li>
  <li>Jamie Reston</li>
  <li>Jamie Reston</li>
</ul>
<article class="abs profile">
  <div class="portrait" role="img" aria-label="Portrait of team member in a suit"></div>
  <div>
    <h3>Martin Averly, <span>Executive Partner</span></h3>
    <p>Martin leads client strategy and product direction at Wendmar Digital. He has spent fifteen years working with outdoor media owners, helping them move from spreadsheets to connected booking and reporting systems. He enjoys turning complex inventory rules into tools that feel simple, and he keeps every project focused on measurable results for sales teams, planners and the people who run the sites each day.</p>
  </div>
</article>
<div class="abs rule" style="top:1240px"></div>

<h2 class="abs section-title" style="top:1262px">Services</h2>
<p class="abs lede" style="top:1324px">We design and build booking platforms, inventory planners, map-based site tools and reporting dashboards for media owners and agencies. Every project starts with a short discovery phase, then moves through prototypes, testing and staged releases. We also offer hosting, support and ongoing improvement plans, so your platform keeps pace with new formats, new data sources and the changing way buyers plan outdoor and digital campaigns across the country.</p>
<div class="abs rule" style="top:1440px"></div>

<h2 class="abs section-title" style="top:1470px">Experience</h2>
<section class="abs work">
  <article class="card">
    <div class="shot" role="img" aria-label="Screenshot of an outdoor advertising website with colourful billboard artwork" style="background:linear-gradient(135deg,#2f8fd8,#8a3fc4 55%,#e24a8c)"></div>
    <div class="caption featured"><h4>Kestrel Outdoor</h4><p>A bold and responsive website for a national outdoor network that highlights its premium formats and growing audience.</p></div>
  </article>
  <article class="card">
    <div class="shot" role="img" aria-label="Hands holding up bidding paddles with brand signs" style="background:linear-gradient(160deg,#f3f3f3,#d7dadd)"></div>
    <div class="caption"><h4>Marketing Bidding Platform</h4><p>An online marketplace where suppliers bid on marketing work, with clear workflows, tender tracking and contract management.</p></div>
  </article>
  <article class="card">
    <div class="shot" role="img" aria-label="Media website screenshots shown on a phone and tablet" style="background:linear-gradient(135deg,#2d2f33,#5c6066 60%,#3a3d42)"></div>
    <div class="caption"><h4>Lumo Media</h4><p>Bright and bold website that clearly guides visitors to find out more about the network, with a depth of content and resources that encourage repeat visits.</p></div>
  </article>
  <article class="card">
    <div class="shot" role="img" aria-label="Office team at work behind a large product title" style="background:linear-gradient(135deg,#6b6e73,#b4b7bb 50%,#5d6066)"></div>
    <div class="caption"><h4>Taskfield</h4><p>A simple task and rostering tool that helps field crews plan their week and share updates from every site.</p></div>
  </article>
  <article class="card">
    <div class="shot" role="img" aria-label="Local search app screens over a city map" style="background:linear-gradient(135deg,#dfe7ee,#9fb9cf 55%,#7f98ad)"></div>
    <div class="caption"><h4>Pintra - Local Search Engine</h4><p>A location based social network where people ask questions, get answers and share local results by map and listing.</p></div>
  </article>
  <article class="card">
    <div class="shot" role="img" aria-label="Collage of geography learning app screens" style="background:linear-gradient(135deg,#eef0f2,#c5cfd8 50%,#d9a24c)"></div>
    <div class="caption"><h4>Offgrid</h4><p>A fun geography learning app built with interactive maps, quizzes and progress tracking for curious students.</p></div>
  </article>
</section>

<footer class="abs footer">
  <div class="abs contact">
    <h5>Consultation / Quote...</h5>
    <p class="intro">Curious about what we can do to help your business? Then please get in touch!</p>
    <div class="row">
      <svg width="10" height="13" viewBox="0 0 10 14"><path fill="#ccc" d="M5 0a5 5 0 0 0-5 5c0 3.8 5 9 5 9s5-5.2 5-9a5 5 0 0 0-5-5zm0 7a2 2 0 1 1 0-4 2 2 0 0 1 0 4z"/></svg>
      <span>Wendmar Digital Pty Ltd<br>Suite 4, Level 9, Harbour Row Tower,<br>12 Keel Street - Sydney NSW 2000 Australia</span>
    </div>
    <div class="row">
      <svg width="11" height="11" viewBox="0 0 24 24"><path fill="#ccc" d="M6.6 10.8a15 15 0 0 0 6.6 6.6l2.2-2.2a1 1 0 0 1 1-.25 11.4 11.4 0 0 0 3.6.57 1 1 0 0 1 1 1V20a1 1 0 0 1-1 1A17 17 0 0 1 3 4a1 1 0 0 1 1-1h3.5a1 1 0 0 1 1 1c0 1.25.2 2.45.57 3.57a1 1 0 0 1-.25 1z"/></svg>
      <span>02 8100 2471</span>
    </div>
    <div class="row">
      <svg width="12" height="10" viewBox="0 0 12 9"><rect x=".5" y=".5" width="11" height="8" fill="none" stroke="#ccc"/><path d="m.5.5 5.5 4.5L11.5.5" fill="none" stroke="#ccc"/></svg>
      <span>info@wendmardigital.example</span>
    </div>
  </div>
  <form class="abs quote-form">
    <div class="field">First Name</div>
    <div class="field">Last Name</div>
    <div class="field">Email</div>
    <div class="field">Phone Number</div>
    <div class="field tall">Details of Inquiry</div>
    <div class="submit">SUBMIT</div>
  </form>
  <div class="abs copyright">Copyright 2014 Wendmar Digital. All Rights Reserved</div>
</footer>

</body>
</html>
```